50th Invite

Design a 50th birthday invite.

Key essentials to communicate are:

Date: 14 December 2019
Time: 7pm for 7.30pm departure
Birthday person: Glen
Theme: Boat Party
Location: Berth K4 27, Fernquay

Other than that will leave to your creativity. Just for clarity, the above is info to be communicated somehow on the invite, I dont want it to be simply copied.

i would like a luxury boat theme, think Miami, Bahamas etc etc, photos or drawings OK

```html
<!DOCTYPE html>
<html lang="en">
<head>
<meta charset="utf-8">
<title>Glen's 50th Birthday Party Invite</title>
<link rel="stylesheet" href="https://fonts.googleapis.com/css2?family=Nunito:wght@800&family=Kaushan+Script&family=Oswald:wght@600&family=Yellowtail&family=Playfair+Display:wght@600&display=swap">
<style>
  :root {
    --backdrop: #b4b4b4;
    --paper: #ffffff;
    --gold-light: #f4dc8c;
    --gold: #e8b43a;
    --gold-deep: #c98a12;
    --script-gold: #f2b926;
    --pink: #e8559a;
    --teal-ink: #0f5b63;
    --sky: #5cc0cc;
    --sea-light: #2f8fa8;
    --sea-deep: #0d4f6a;
  }
  * { margin: 0; padding: 0; box-sizing: border-box; }
  html, body {
    width: 1198px; height: 1200px; overflow: hidden;
    background: var(--backdrop);
  }
  .invite {
    position: absolute; left: 189px; top: 50px;
    width: 820px; height: 1100px;
    background: var(--paper);
    overflow: hidden;
    box-shadow: 0 6px 18px rgba(0,0,0,.18);
  }
  .invite svg.frame { position: absolute; inset: 0; }
  .numeral { font-family: "Nunito", sans-serif; font-weight: 800; }
  .ordinal { font-family: "Playfair Display", serif; font-weight: 600; }
  .headline {
    position: absolute; left: 120px; top: 325px; width: 560px;
    font-family: "Kaushan Script", cursive; color: var(--script-gold);
    font-size: 138px; line-height: 140px; text-align: center; font-weight: 400;
  }
  .headline span { display: block; white-space: nowrap; }
  .headline .second { padding-left: 70px; }
  .invitation-line {
    position: absolute; left: 30px; width: 500px; text-align: center;
    color: var(--pink); white-space: nowrap;
  }
  .kicker {
    top: 668px; font-family: "Oswald", sans-serif; font-weight: 600;
    font-size: 24px; line-height: 30px; letter-spacing: .3px; text-transform: uppercase;
  }
  .honoree {
    top: 700px; font-family: "Yellowtail", "Kaushan Script", cursive; font-size: 34px; line-height: 44px;
  }
  .details {
    position: absolute; left: 30px; top: 758px; width: 500px; height: 102px;
    border-top: 2px solid var(--teal-ink); border-bottom: 2px solid var(--teal-ink);
    display: flex; color: var(--teal-ink);
    font-family: "Oswald", sans-serif; font-weight: 600;
  }
  .date {
    width: 190px; flex: none; border-right: 2px solid var(--teal-ink);
    text-align: center; font-size: 38px; line-height: 42px; padding-top: 6px;
  }
  .venue { padding: 10px 0 0 10px; white-space: nowrap; }
  .venue .place { font-size: 29px; line-height: 40px; }
  .venue .time { font-size: 21px; line-height: 34px; }
</style>
</head>
<body>
  <main class="invite">
    <svg class="frame" width="820" height="1100" viewBox="0 0 820 1100">
      <defs>
        <linearGradient id="gold-foil" x1="0" y1="0" x2="1" y2="0">
          <stop offset="0" stop-color="var(--gold-deep)"/>
          <stop offset=".3" stop-color="var(--gold-light)"/>
          <stop offset=".6" stop-color="var(--gold)"/>
          <stop offset="1" stop-color="var(--gold-deep)"/>
        </linearGradient>
        <linearGradient id="sea" x1="0" y1="0" x2="1" y2="1">
          <stop offset="0" stop-color="var(--sea-light)"/>
          <stop offset="1" stop-color="var(--sea-deep)"/>
        </linearGradient>
      </defs>

      <rect class="gift-art" role="img" aria-label="Pink line drawing of a wrapped gift box" x="0" y="60" width="170" height="170" rx="10" fill="#fbe2ee"/>
      <rect class="streamer-art" role="img" aria-label="Teal curled party streamers" x="670" y="130" width="120" height="200" rx="10" fill="#dff2f5"/>
      <rect class="cake-art" role="img" aria-label="Teal line drawing of a tiered birthday cake" x="12" y="440" width="140" height="160" rx="10" fill="#dff2f5"/>
      <rect class="balloon-art" role="img" aria-label="Pink line drawing of a balloon with ribbon bows" x="630" y="480" width="170" height="320" rx="10" fill="#fbe2ee"/>

      <text class="numeral" x="160" y="285" font-size="330" fill="none" stroke="url(#gold-foil)" stroke-width="7" letter-spacing="-10">50</text>
      <text class="ordinal" x="615" y="82" font-size="48" fill="url(#gold-foil)">TH</text>
      <line x1="0" y1="318" x2="800" y2="308" stroke="url(#gold-foil)" stroke-width="5"/>

      <path class="boat-photo" role="img" aria-label="Aerial photo of a party boat on blue water with guests swimming"
            d="M20 935 C 300 905, 540 885, 640 850 S 780 800, 820 790 L 820 1100 L 20 1100 Z" fill="url(#sea)"/>
      <path d="M20 935 C 300 905, 540 885, 640 850 S 780 800, 820 790" fill="none" stroke="var(--pink)" stroke-width="7"/>
    </svg>

    <h1 class="headline"><span>Birthday</span><span class="second">Party</span></h1>

    <p class="invitation-line kicker">Join us to celebrate</p>
    <p class="invitation-line honoree">Glen's 50th Birthday</p>

    <section class="details">
      <div class="date">DECEMBER<br>14</div>
      <div class="venue">
        <div class="place">Berth K4 27, Fernquay</div>
        <div class="time">7 pm for 7.30 pm Departure</div>
      </div>
    </section>
  </main>
</body>
</html>
```